The Festival! Poster for an Annual Dance Showcase

We are looking for a dynamic festival/concert style poster for our annual dance showcase featuring at least one image of our dancers and the main information. The main image should be one of the dancers but there can be a collage of the dancers or smaller images around the poster. I have included some reference images but it can vary from them.

Must have this information;
Date - May 22-26
Location - Mabel Corwin Hale Theatre
Tickets - Vondo.bm

Target Market(s)

Parents and people who love dance

Industry/Entity Type

Dance

Font styles to use
Sans Serif

Colors
E54698
E96AAD
F1A4CE
F9D9EA
FCEFF6

Requirements
Must have
• Logo, Date and Location, Picture of Dancer

```html
<!DOCTYPE html>
<html lang="en">
<head>
<meta charset="utf-8">
<title>Tempo Lane School of Dance — Annual Dance Showcase</title>
<link href="https://fonts.googleapis.com/css2?family=League+Spartan:wght@400;700;800&display=swap" rel="stylesheet">
<style>
  :root {
    --pink: #ec068d;
    --orange: #e09e26;
    --green: #52b848;
    --blue: #3a67b1;
    --brown: #8a6f3b;
    --ink: #231f20;
    --white: #ffffff;
  }
  * { box-sizing: border-box; margin: 0; padding: 0; }
  html, body { width: 1200px; height: 1200px; overflow: hidden; background: var(--white); }
  body { position: relative; font-family: "League Spartan", sans-serif; }

  .poster { position: absolute; left: 200px; top: 34px; width: 806px; height: 1141px; background: var(--pink); }
  .block { position: absolute; border: 2px solid var(--ink); }

  .masthead { position: absolute; left: 232px; top: 65px; width: 743px; height: 193px; }
  .masthead svg { position: absolute; inset: 0; }
  .brand { position: absolute; left: 254px; top: 87px; width: 699px; height: 120px;
    display: flex; align-items: center; justify-content: center; gap: 18px; color: var(--pink); }
  .brand-dot { width: 36px; height: 36px; border-radius: 50%; background: var(--pink); }
  .brand-name { font-weight: 800; text-transform: uppercase; line-height: .9; }
  .brand-name .big { display: block; font-size: 56px; letter-spacing: -1px; }
  .brand-name .small { display: block; font-size: 31px; margin-top: 6px; }

  .side { width: 142px; height: 201px; }
  .panel-orange { background: radial-gradient(ellipse 38% 46% at 50% 55%, var(--blue) 0%, rgba(58,103,177,.55) 45%, rgba(58,103,177,0) 100%), var(--orange); }
  .panel-blue { background: radial-gradient(ellipse 38% 46% at 50% 55%, var(--orange) 0%, rgba(224,158,38,.55) 45%, rgba(224,158,38,0) 100%), var(--blue); }
  .panel-green { background: radial-gradient(ellipse 38% 46% at 50% 55%, var(--blue) 0%, rgba(58,103,177,.55) 45%, rgba(58,103,177,0) 100%), var(--green); }

  .stage { position: absolute; left: 391px; top: 275px; width: 425px; height: 638px; }
  .stage svg { position: absolute; inset: 0; }
  .dancers { position: absolute; left: 96px; top: 190px; width: 232px; height: 432px;
    border-radius: 116px 116px 14px 14px;
    background: linear-gradient(170deg, var(--orange) 0%, #e8589a 40%, var(--pink) 70%, var(--pink) 100%); }

  .badge { position: absolute; left: 532px; top: 200px; width: 325px; height: 175px;
    background: var(--orange); border: 2px solid var(--ink);
    border-radius: 162px 162px 22px 22px / 170px 170px 22px 22px;
    transform-origin: 50% 100%; transform: rotate(-22deg);
    display: flex; flex-direction: column; align-items: center; justify-content: flex-end;
    padding-bottom: 18px; color: var(--pink); text-transform: uppercase; line-height: .85; }
  .badge .annual, .badge .showcase { font-weight: 800; font-size: 27px; }
  .badge .dance { font-weight: 400; font-size: 64px; margin-top: 2px; }

  .date-band { left: 232px; top: 927px; width: 743px; height: 75px;
    background: var(--blue); color: var(--orange); display: flex; align-items: center; justify-content: center;
    font-weight: 800; font-size: 52px; word-spacing: 6px; padding-top: 6px; }

  .venue-box { left: 232px; top: 1017px; width: 743px; height: 124px; background: var(--orange); color: var(--blue);
    text-align: center; text-transform: uppercase; font-weight: 800; }
  .venue-name { margin-top: 24px; font-size: 38px; }
  .venue-site { margin-top: 10px; font-size: 19px; }
</style>
</head>
<body>
  <div class="poster"></div>

  <header class="masthead">
    <svg width="743" height="193" viewBox="0 0 743 193">
      <polygon points="1,1 742,1 721,22 22,22" fill="var(--orange)" stroke="var(--ink)" stroke-width="2"/>
      <polygon points="1,1 22,22 22,171 1,192" fill="var(--orange)" stroke="var(--ink)" stroke-width="2"/>
      <polygon points="742,1 742,192 721,171 721,22" fill="var(--green)" stroke="var(--ink)" stroke-width="2"/>
      <polygon points="1,192 22,171 721,171 742,192" fill="var(--blue)" stroke="var(--ink)" stroke-width="2"/>
      <rect x="22" y="22" width="699" height="149" fill="var(--ink)" stroke="var(--ink)" stroke-width="2"/>
    </svg>
  </header>
  <div class="brand">
    <span class="brand-dot"></span>
    <h1 class="brand-name"><span class="big">Tempo Lane</span><span class="small">School of Dance</span></h1>
  </div>

  <div class="block side panel-orange" style="left:232px;top:275px" role="img" aria-label="Dancer in a blue dress reaching upward"></div>
  <div class="block side panel-blue" style="left:232px;top:494px" role="img" aria-label="Dancer in a backbend"></div>
  <div class="block side panel-green" style="left:232px;top:711px" role="img" aria-label="Dancer balancing on one leg"></div>
  <div class="block side panel-orange" style="left:832px;top:275px" role="img" aria-label="Dancer in a low lunge"></div>
  <div class="block side panel-blue" style="left:832px;top:494px" role="img" aria-label="Dancer in an arabesque"></div>
  <div class="block side panel-green" style="left:832px;top:711px" role="img" aria-label="Dancer seated with a flowing skirt"></div>

  <section class="stage">
    <svg width="425" height="638" viewBox="0 0 425 638">
      <rect x="1" y="1" width="423" height="636" fill="var(--green)" stroke="var(--ink)" stroke-width="2"/>
      <path d="M20,514 V215 A192,192 0 0 1 404,215 V514 Z" fill="var(--brown)" stroke="var(--ink)" stroke-width="2"/>
      <path d="M53,514 V215 A159,159 0 0 1 371,215 V514 Z" fill="var(--green)" stroke="var(--ink)" stroke-width="2"/>
      <path d="M86,514 V215 A126,126 0 0 1 338,215 V514 Z" fill="var(--blue)" stroke="var(--ink)" stroke-width="2"/>
      <rect x="1" y="514" width="423" height="123" fill="var(--blue)" stroke="var(--ink)" stroke-width="2"/>
    </svg>
    <div class="dancers" role="img" aria-label="Two dancers in pink costumes posing with arms outstretched"></div>
  </section>

  <div class="badge">
    <span class="annual">Annual</span>
    <span class="dance">Dance</span>
    <span class="showcase">Showcase</span>
  </div>

  <div class="block date-band">2025 MAY 22-26</div>

  <div class="block venue-box">
    <p class="venue-name">Mabel Corwin Hale Theatre</p>
    <p class="venue-site">www.vondo.bm</p>
  </div>
</body>
</html>
```